Speisekarten für ein modernes, junges Café
Zielgruppe
Wir suchen eine Speisekarte für ein modernes, junges Café. Frühstück, kleine Speisen, Snacks und Getränke stehen auf der Karte. Unsere Zielgruppe sind hauptsächlich junge Menschen bis 40 Jahre.
Die Speisekarte sollte immer änderbar sein ( nur Text bei neuen Speisen zum Beispiel )
Aufgabenstellung
Das Logo kann und soll gerne mit eingefügt werden. Eventuell gleich auf dem Deckblatt.
Generell bin ich offen für junge, coole Ideen.
Unten die Themen/ grobe Überschriften
Kaffee und Espresso
Frühstücksvariationen
Eierspeisen
Frühstück zum löffeln
Pancakes
Extras zum Frühstück
Snacks/ kleine Speisen
-die Kurbel. Drinks
-die Kurbel. Wein & Bier )
((Kinderspeisekarte:
zusätzlich noch ein extra Blatt für die Kinder zum ausmalen mit den illustrierten Bildern auch im modernen Stil ))

```html
<!DOCTYPE html>
<html lang="de">
<head>
<meta charset="utf-8">
<title>die Kurbel. – Frühstückskarte</title>
<link rel="stylesheet" href="https://fonts.googleapis.com/css2?family=Lobster&family=Arvo:wght@700&family=Libre+Baskerville:ital,wght@0,400;1,700&display=swap">
<style>
  :root{
    --bg:#dcdcdc;
    --paper:#e6ddd0;
    --paper-shade:#d8cbb9;
    --ink:#3e2c22;
    --band:#3b2e26;
    --illu:#c9b9a3;
  }
  *{box-sizing:border-box;margin:0;padding:0}
  html,body{width:1200px;height:1014px;overflow:hidden;background:var(--bg)}
  .canvas{position:relative;width:1200px;height:1014px}
  .page{position:absolute;top:217px;width:448px;height:632px;
    background:radial-gradient(ellipse at 50% 40%,#ece4d8 0%,var(--paper) 60%,var(--paper-shade) 100%);
    color:var(--ink);overflow:hidden}
  .page--front{left:135px}
  .page--back{left:636px}
  .band{position:absolute;left:0;width:100%;background:var(--band)}
  .band--top{top:0;height:14px}
  .band--bottom{bottom:0;height:13px}
  .illu{position:absolute;background:var(--illu);opacity:.55;border-radius:6px}
  .title{position:absolute;font-family:"Lobster",cursive;font-size:44px;line-height:1;color:var(--ink)}
  .logo{position:absolute;left:321px;top:43px;width:82px;height:82px;border-radius:50%;
    background:var(--paper);border:2px solid var(--ink);display:flex;align-items:center;justify-content:center;
    font-family:"Libre Baskerville",serif;font-size:12px;color:var(--ink)}
  .heading{position:absolute;font-family:"Lobster",cursive;font-size:24px;line-height:1;color:var(--ink)}
  .rule{position:absolute;height:1.5px;background:var(--ink)}
  .rule::before,.rule::after{content:"";position:absolute;top:-2.5px;width:5px;height:5px;border:1.2px solid var(--ink);border-radius:50%;background:var(--paper)}
  .rule::before{left:-5px}
  .rule::after{right:-5px}
  .subhead{position:absolute;font-family:"Arvo",serif;font-weight:700;font-size:12.5px;color:var(--ink)}
  .item{position:absolute;display:flex;align-items:baseline;font-family:"Libre Baskerville",serif;font-size:10px;line-height:1;color:var(--ink)}
  .item .leader{flex:1;border-bottom:1.2px dashed var(--ink);margin:0 5px;transform:translateY(-2px)}
  .item--plain .leader{display:none}
  .info{position:absolute;left:143px;top:505px;width:196px;height:70px;border:2px solid var(--ink);
    padding:8px 10px;font-family:"Libre Baskerville",serif;font-size:10px;line-height:1.55;color:var(--ink)}
  .info .social{font-weight:700;font-style:italic;font-size:11px}
</style>
</head>
<body>
<div class="canvas">

  <!-- Front page -->
  <section class="page page--front">
    <div class="band band--top"></div>
    <h1 class="title" style="left:22px;top:28px">Frühstücks-</h1>
    <div class="title" style="left:80px;top:82px">Karte</div>
    <div class="logo">die Kurbel.</div>

    <div class="illu" role="img" aria-label="Gezeichnete Schale" style="left:285px;top:125px;width:38px;height:22px"></div>
    <div class="illu" role="img" aria-label="Gezeichneter Löffel" style="left:213px;top:144px;width:28px;height:28px"></div>
    <div class="illu" role="img" aria-label="Gezeichnete Kaffeetasse mit Latte Art" style="left:42px;top:142px;width:45px;height:36px"></div>

    <h2 class="heading" style="left:86px;top:162px">Kaffee</h2>
    <div class="rule" style="left:44px;top:188px;width:163px"></div>
    <div class="item" style="left:33px;top:213px;width:174px"><span>Cappuccino</span><span class="leader"></span><span>€ 3,50</span></div>
    <div class="item" style="left:33px;top:236px;width:174px"><span>Espresso</span><span class="leader"></span><span>€ 3,50</span></div>
    <div class="item" style="left:33px;top:260px;width:174px"><span>Latte Macchiato</span><span class="leader"></span><span>€ 3,50</span></div>
    <div class="item" style="left:33px;top:283px;width:174px"><span>Haferlatte</span><span class="leader"></span><span>€ 3,50</span></div>

    <div class="illu" role="img" aria-label="Gezeichnetes Croissant" style="left:172px;top:311px;width:44px;height:38px"></div>
    <h2 class="heading" style="left:68px;top:352px">Frühstück</h2>
    <div class="rule" style="left:44px;top:373px;width:163px"></div>
    <h3 class="subhead" style="left:33px;top:394px">Eierspeisen</h3>
    <div class="item" style="left:33px;top:423px;width:174px"><span>Rührei</span><span class="leader"></span><span>€ 3,50</span></div>
    <div class="item" style="left:33px;top:446px;width:174px"><span>Pochiertes Ei</span><span class="leader"></span><span>€ 3,50</span></div>
    <div class="item" style="left:33px;top:469px;width:174px"><span>Oma-Pfanderl</span><span class="leader"></span><span>€ 3,50</span></div>

    <h3 class="subhead" style="left:248px;top:161px">Frühstück zum Löffeln</h3>
    <div class="item" style="left:248px;top:191px;width:166px"><span>Müsli mit Nüssen</span><span class="leader"></span><span>€ 3,50</span></div>
    <div class="item" style="left:248px;top:214px;width:166px"><span>Joghurtmüsli</span><span class="leader"></span><span>€ 3,50</span></div>
    <div class="item" style="left:248px;top:237px;width:166px"><span>Müsli mit Früchten</span><span class="leader"></span><span>€ 3,50</span></div>
    <div class="item" style="left:248px;top:260px;width:166px"><span>Veganes Müsli</span><span class="leader"></span><span>€ 3,50</span></div>

    <h3 class="subhead" style="left:248px;top:290px">Pancakes</h3>
    <div class="item" style="left:248px;top:319px;width:166px"><span>Erdbeer-Pancakes</span><span class="leader"></span><span>€ 3,50</span></div>
    <div class="item" style="left:248px;top:342px;width:166px"><span>Zwiebel Pancakes</span><span class="leader"></span><span>€ 3,50</span></div>
    <div class="item" style="left:248px;top:366px;width:166px"><span>Pancakes mit Schinken</span><span class="leader"></span><span>€ 3,50</span></div>
    <div class="item" style="left:248px;top:389px;width:166px"><span>Fluffy Pancake</span><span class="leader"></span><span>€ 3,50</span></div>

    <h3 class="subhead" style="left:248px;top:418px">Extras</h3>
    <div class="illu" role="img" aria-label="Gezeichnetes Trinkglas" style="left:387px;top:413px;width:28px;height:35px"></div>
    <div class="item item--plain" style="left:248px;top:447px;width:166px"><span>Frisch gepresster</span></div>
    <div class="item" style="left:248px;top:470px;width:166px"><span>Orangensaft</span><span class="leader"></span><span>€ 3,50</span></div>
    <div class="item" style="left:248px;top:493px;width:166px"><span>Ein Glas Milch</span><span class="leader"></span><span>€ 3,50</span></div>
    <div class="item" style="left:248px;top:516px;width:166px"><span>Marmeladeglas</span><span class="leader"></span><span>€ 3,50</span></div>

    <div class="illu" role="img" aria-label="Gezeichnete Kaffeetasse mit Untertasse" style="left:121px;top:509px;width:64px;height:56px"></div>
    <div class="illu" role="img" aria-label="Gezeichnete Kaffeebohnen entlang des unteren Randes" style="left:0;top:560px;width:448px;height:59px;border-radius:0;background:linear-gradient(180deg,rgba(201,185,163,0) 0%,var(--illu) 60%)"></div>
    <div class="band band--bottom"></div>
  </section>

  <!-- Back page -->
  <section class="page page--back">
    <div class="band band--top"></div>

    <div class="illu" role="img" aria-label="Gezeichnete Teekanne" style="left:191px;top:37px;width:41px;height:38px"></div>
    <h2 class="heading" style="left:108px;top:52px">Tee</h2>
    <div class="rule" style="left:40px;top:80px;width:166px"></div>
    <div class="item" style="left:34px;top:105px;width:176px"><span>Früchtetee</span><span class="leader"></span><span>€ 3,50</span></div>
    <div class="item" style="left:34px;top:128px;width:176px"><span>English Breakfast</span><span class="leader"></span><span>€ 3,50</span></div>
    <div class="item" style="left:34px;top:151px;width:176px"><span>Kräutertee</span><span class="leader"></span><span>€ 3,50</span></div>

    <h2 class="heading" style="left:292px;top:52px">Snacks</h2>
    <div class="rule" style="left:246px;top:80px;width:169px"></div>
    <div class="item" style="left:242px;top:105px;width:176px"><span>Belegtes Brot</span><span class="leader"></span><span>€ 3,50</span></div>
    <div class="item" style="left:242px;top:128px;width:176px"><span>Lachsbrötchen</span><span class="leader"></span><span>€ 3,50</span></div>
    <div class="item" style="left:242px;top:151px;width:176px"><span>Suppe</span><span class="leader"></span><span>€ 3,50</span></div>
    <div class="illu" role="img" aria-label="Gezeichneter Burger" style="left:366px;top:170px;width:51px;height:50px"></div>

    <h2 class="heading" style="left:53px;top:197px">Alkoholfrei</h2>
    <div class="rule" style="left:40px;top:223px;width:166px"></div>
    <div class="item" style="left:33px;top:245px;width:177px"><span>Mineralwasser</span><span class="leader"></span><span>€ 3,50</span></div>
    <div class="item" style="left:33px;top:268px;width:177px"><span>Almtaler</span><span class="leader"></span><span>€ 3,50</span></div>
    <div class="item" style="left:33px;top:291px;width:177px"><span>Fruvo div.</span><span class="leader"></span><span>€ 3,50</span></div>

    <div class="illu" role="img" aria-label="Gezeichnetes Weinglas" style="left:261px;top:199px;width:28px;height:56px"></div>
    <h2 class="heading" style="left:282px;top:240px">Wein</h2>
    <div class="rule" style="left:246px;top:268px;width:168px"></div>
    <div class="item" style="left:238px;top:293px;width:180px"><span>Zweigelt 1/8</span><span class="leader"></span><span>€ 3,50</span></div>
    <div class="item" style="left:238px;top:316px;width:180px"><span>Merlot 1/8</span><span class="leader"></span><span>€ 3,50</span></div>
    <div class="item" style="left:238px;top:340px;width:180px"><span>1 Kanne Hauswein</span><span class="leader"></span><span>€ 3,50</span></div>

    <h2 class="heading" style="left:99px;top:332px">Bier</h2>
    <div class="illu" role="img" aria-label="Gezeichneter Bierkrug" style="left:168px;top:321px;width:31px;height:32px"></div>
    <div class="rule" style="left:40px;top:360px;width:166px"></div>
    <div class="item" style="left:34px;top:385px;width:180px"><span>Craft Beer</span><span class="leader"></span><span>€ 3,50</span></div>
    <div class="item" style="left:34px;top:408px;width:180px"><span>Radler</span><span class="leader"></span><span>€ 3,50</span></div>
    <div class="item" style="left:34px;top:431px;width:180px"><span>Weißbier</span><span class="leader"></span><span>€ 3,50</span></div>

    <div class="illu" role="img" aria-label="Gezeichneter Kaffeezweig mit Kirschen" style="left:371px;top:404px;width:77px;height:95px"></div>
    <div class="illu" role="img" aria-label="Gezeichneter Kaffeebecher zum Mitnehmen" style="left:99px;top:464px;width:44px;height:54px"></div>
    <div class="illu" role="img" aria-label="Gezeichneter Sack mit Kaffeebohnen und Schaufel" style="left:26px;top:505px;width:104px;height:114px"></div>

    <div class="info">
      <p>Öffnungszeiten:</p>
      <p>Di-So 7-20Uhr | Montag Ruhetag</p>
      <p class="social">Bildkanal: @socialmedia</p>
    </div>

    <div class="illu" role="img" aria-label="Gezeichnetes Besteck: Löffel, Messer, Gabel" style="left:353px;top:568px;width:50px;height:51px"></div>
    <div class="band band--bottom"></div>
  </section>

</div>
</body>
</html>
```